依頼詳細
作成している原稿があるので別途添付いたします。
記載項目
作成原稿にすべて入れています。
サイズ
A4
ページ数
片面
希望イメージ
シンプル 複雑
単色 カラフル
暗い 明るい
日常 高級
遊び心 厳粛
未来的 伝統的
女性的 男性的
希望する色
無彩色系、無彩色系ですが明るめの色もあれば見たいです
納品ファイル
• イラストレーター形式 (.ai)
• PNG形式 (.png)
補足説明

```html
<!DOCTYPE html>
<html lang="ja">
<head>
<meta charset="utf-8">
<title>ご縁つむぎ学舎 開校プレ講演会</title>
<link rel="stylesheet" href="https://fonts.googleapis.com/css2?family=Noto+Sans+JP:wght@400;700;900&family=Yuji+Boku&family=Great+Vibes&display=swap">
<style>
:root{
  --ink:#1e1e1e;
  --charcoal:#2d2d2d;
  --smoke:#4a4a4a;
  --paper:#ffffff;
  --mist:#ececec;
  --line:#9a9a9a;
  --red:#d2261e;
  --orange:#f08a1c;
  --text:#222;
}
*{margin:0;padding:0;box-sizing:border-box}
html,body{width:849px;height:1200px;overflow:hidden;background:var(--paper)}
body{font-family:"Noto Sans JP",sans-serif;color:var(--text)}
.flyer{position:relative;width:849px;height:1200px;overflow:hidden;background:var(--paper)}

.hero{position:absolute;left:0;top:0;width:849px;height:385px;background:linear-gradient(180deg,#333 0%,var(--ink) 100%)}
.hero-photo{position:absolute;right:0;top:40px;width:400px;height:345px;background:radial-gradient(ellipse at 55% 45%,#8a8a8a 0%,#4d4d4d 55%,#262626 100%)}
.hero-event{position:absolute;top:12px;left:0;width:100%;text-align:center;color:var(--paper);font-size:14px;font-weight:700;letter-spacing:1px}
.hero-event .school{color:var(--red)}
.hero-name{position:absolute;top:12px;right:22px;color:var(--paper);font-size:15px;font-weight:700;letter-spacing:2px}
.headline{position:absolute;left:30px;top:58px;font-family:"Yuji Boku",serif;color:var(--paper);line-height:1.08;text-shadow:0 2px 4px rgba(0,0,0,.6)}
.headline .l1{display:block;font-size:62px}
.headline .l2{display:block;font-size:62px;padding-left:36px}
.headline .l3{display:block;font-size:82px;padding-left:36px}
.headline .accent{color:var(--red)}

.switch{position:absolute;left:0;top:395px;width:849px;text-align:center}
.switch-lead{font-size:19px;font-weight:700;letter-spacing:1px}
.switch-title{display:inline-block;margin-top:8px;padding:4px 26px;border:2px solid var(--ink);font-size:27px;font-weight:900;letter-spacing:2px}

.rules{position:absolute;left:28px;top:490px;width:793px;display:grid;grid-template-columns:1fr 1fr;gap:8px 10px;padding:10px;background:var(--mist)}
.rule{display:flex;align-items:center;height:34px;background:var(--paper);border:1px solid var(--line)}
.rule-num{width:34px;height:34px;background:var(--charcoal);color:var(--paper);font-weight:900;font-size:18px;display:flex;align-items:center;justify-content:center}
.rule-text{padding-left:12px;font-size:17px;font-weight:700}

.event{position:absolute;left:28px;top:600px;width:420px}
.event-date{display:flex;align-items:flex-end;gap:8px;color:var(--red);font-weight:900}
.event-date .day{font-size:66px;line-height:1}
.event-date .week{font-size:26px;padding-bottom:6px}
.badge-open{position:absolute;left:258px;top:6px;width:54px;height:54px;border-radius:50%;background:var(--orange);color:var(--paper);font-size:12px;font-weight:700;display:flex;align-items:center;justify-content:center;text-align:center;line-height:1.2}
.event-time{margin-top:4px;font-size:20px;font-weight:700}
.event-time span{margin-right:18px}
.event-venue{margin-top:14px;font-size:14px;line-height:1.6}
.event-venue dt{display:inline-block;width:56px;padding:1px 0;background:var(--charcoal);color:var(--paper);text-align:center;font-size:12px;margin-right:8px}
.event-venue div{margin-bottom:4px}
.event-tel{display:flex;align-items:center;gap:8px;font-size:30px;font-weight:900;margin-top:2px}
.event-host{font-size:12px;margin-top:6px}

.school-box{position:absolute;left:460px;top:596px;width:361px;height:288px;border:1px solid var(--line);background:var(--mist);padding:14px 14px 10px}
.school-box h3{font-size:17px;font-weight:900;color:var(--charcoal)}
.school-box .sub{font-size:11px;margin-top:2px}
.badge-all{position:absolute;right:14px;top:10px;width:52px;height:52px;border-radius:50%;background:var(--red);color:var(--paper);font-size:12px;font-weight:700;display:flex;align-items:center;justify-content:center;text-align:center;line-height:1.2}
.schedule{margin-top:16px;list-style:none;font-size:11.5px;line-height:1.85}
.schedule li{border-bottom:1px dotted var(--line)}
.schedule b{display:inline-block;width:64px;color:var(--red)}
.school-time{margin-top:10px;font-size:13px;font-weight:700}
.school-place{font-size:12px}

.tickets{position:absolute;left:0;top:900px;width:849px;height:300px;background:var(--charcoal);color:var(--paper)}
.tickets-title{position:absolute;left:28px;top:8px;font-family:"Great Vibes",cursive;font-size:56px}
.prices{position:absolute;left:30px;top:90px;width:250px;font-size:13px;line-height:1.9}
.prices .row{display:flex;gap:10px}
.prices .label{width:50px;background:var(--paper);color:var(--charcoal);text-align:center;font-weight:700;font-size:12px;height:20px;line-height:20px;margin-top:3px}
.apply{position:absolute;left:300px;top:30px;width:320px;font-size:12px;line-height:1.7}
.apply-head{display:inline-block;background:var(--paper);color:var(--charcoal);font-weight:700;padding:2px 8px;margin-bottom:6px}
.bank{position:absolute;left:300px;top:180px;width:520px;display:grid;grid-template-columns:1fr 1fr;gap:12px;font-size:12px;line-height:1.7}
.bank b{display:block;font-size:13px}
</style>
</head>
<body>
<main class="flyer">

  <section class="hero">
    <div class="hero-photo" role="img" aria-label="マイクを持って語りかける講師の写真"></div>
    <p class="hero-event"><span class="school">ご縁つむぎ学舎前橋校</span>　開校プレ講演会</p>
    <p class="hero-name">山川健人</p>
    <h1 class="headline">
      <span class="l1">「出会いこそ宝である</span>
      <span class="l2">人のご縁で</span>
      <span class="l3"><span class="accent">でっかく</span>生きる」</span>
    </h1>
  </section>

  <section class="switch">
    <p class="switch-lead">今日、あなたの心にスイッチが入ります。</p>
    <p class="switch-title">「4つの鉄板ルール」</p>
  </section>

  <ol class="rules">
    <li class="rule"><span class="rule-num">1</span><span class="rule-text">返事は0.2秒！</span></li>
    <li class="rule"><span class="rule-num">2</span><span class="rule-text">頼まれごとは試されごと！</span></li>
    <li class="rule"><span class="rule-num">3</span><span class="rule-text">出来ない理由を言わない！</span></li>
    <li class="rule"><span class="rule-num">4</span><span class="rule-text">そのうちと言わずできることから！</span></li>
  </ol>

  <section class="event">
    <p class="event-date"><span class="day">7/11</span><span class="week">[Sat]</span></p>
    <div class="badge-open">予約<br>受付中</div>
    <p class="event-time"><span>開演 18:30〜</span><span>会場 18:00〜</span></p>
    <dl class="event-venue">
      <div><dt>会場</dt><dd style="display:inline">北町シティホール</dd></div>
      <div><dt>住所</dt><dd style="display:inline">北町市中央町12-3</dd></div>
    </dl>
    <p class="event-tel">
      <svg width="28" height="28" viewBox="0 0 24 24" aria-hidden="true"><path fill="#2d2d2d" d="M6.6 10.8a15.1 15.1 0 0 0 6.6 6.6l2.2-2.2a1 1 0 0 1 1-.25 11.4 11.4 0 0 0 3.6.57 1 1 0 0 1 1 1V20a1 1 0 0 1-1 1A17 17 0 0 1 3 4a1 1 0 0 1 1-1h3.5a1 1 0 0 1 1 1c0 1.25.2 2.45.57 3.57a1 1 0 0 1-.25 1z"/></svg>
      000-123-4567
    </p>
    <p class="event-host">主催：ご縁つむぎ学舎前橋校事務局</p>
  </section>

  <aside class="school-box">
    <h3>ご縁つむぎ学舎案内</h3>
    <p class="sub">ご縁つむぎ学舎前橋校 開講日程</p>
    <div class="badge-all">全講座<br>開講</div>
    <ul class="schedule">
      <li><b>第1講座</b>9月6日(日)「人に喜ばれる生き方」</li>
      <li><b>第2講座</b>10月4日(日)「ご縁を広げる話し方」</li>
      <li><b>第3講座</b>11月1日(日)「仕事の楽しみ方」</li>
      <li><b>第4講座</b>12月6日(日)「心に届く伝え方」</li>
      <li><b>第5講座</b>1月10日(日)「プロフェッショナル論」</li>
      <li><b>第6講座</b>2月7日(日)「未来をひらく行動力」</li>
    </ul>
    <p class="school-time">時間　13:00〜18:00</p>
    <p class="school-place">会場　北町自治ビル（前橋予定）</p>
  </aside>

  <section class="tickets">
    <h2 class="tickets-title">Tickets</h2>
    <div class="prices">
      <div class="row"><span class="label">一般</span><span>2,500円（前売）<br>3,000円（当日）</span></div>
      <div class="row"><span class="label">学生</span><span>1,000円（前売）<br>1,500円（当日）</span></div>
    </div>
    <div class="apply">
      <span class="apply-head">申し込み・お問い合わせ</span>
      <p>①ホームページにてご受付・お問合せ<br>②メールまたはお電話で下記までご連絡ください<br>「氏名・電話番号・枚数」をお知らせください<br>✉ info@example.jp<br>TEL 090-0000-1111（受付 平日10時〜18時）</p>
    </div>
    <div class="bank">
      <div><b>ひかり銀行</b>記号 10000　番号 12345670<br>口座名　ゴエンツムギガクシャ</div>
      <div><b>みなみ銀行</b>中央支店　普通 0000000<br>口座名　ゴエンツムギ　ヤマカワ</div>
    </div>
  </section>

</main>
</body>
</html>
```